Carpentry and Building Business Card

I'm looking for a business card that is minimalistic and that incorporates the theme of my Velmor logo.
On one side I'd like the VELMOR logo with my details on the other side.
Double sided with curved edges

Target Market(s)

Construction / renovation
Adults

Industry/Entity Type

Tradesman

Contact Information for Business Card

Logo on one side, details on the other

Colors

Designer to choose only greyscale colors for use in the design.

Requirements
Must have
• Nilo Petrakis
VELMOR CONSTRUCT
Carpentry & Building Services
0481236574
Velmorconstruct@brixmail.com
Lic No. 718263D
Nice to have
• Fb and insta icons. @velmorconstruct
Should not have
• No hammer or tool icons please.

No address line.

```html
<!DOCTYPE html>
<html lang="en">
<head>
<meta charset="utf-8">
<title>Velmor Construct – Business Card</title>
<link href="https://fonts.googleapis.com/css2?family=Montserrat:wght@500&family=Lato:wght@400;700&display=swap" rel="stylesheet">
<style>
  :root {
    --page: #d4d4d4;
    --ink: #111111;
    --black: #000000;
    --white: #ffffff;
    --accent: #8c8c8c;
    --accent-light: #bdbdbd;
    --accent-soft: #a6a6a6;
  }
  * { box-sizing: border-box; margin: 0; padding: 0; }
  html, body { width: 1200px; height: 800px; overflow: hidden; }
  body {
    background: var(--page);
    font-family: "Lato", sans-serif;
    display: flex;
    align-items: center;
    justify-content: center;
    gap: 40px;
  }
  .card {
    position: relative;
    width: 540px;
    height: 310px;
    border-radius: 16px;
    overflow: hidden;
    box-shadow: 0 6px 18px rgba(0,0,0,0.18);
  }
  .card-front { background: var(--white); }
  .card-back { background: var(--black); color: var(--white); }

  .brand-mark {
    position: absolute;
    background: var(--accent);
  }
  .wordmark {
    position: absolute;
    font-family: "Montserrat", sans-serif;
    font-weight: 500;
    letter-spacing: 0.28em;
    white-space: nowrap;
  }

  /* Front */
  .card-front .brand-mark { left: 46px; top: 112px; width: 46px; height: 46px; }
  .card-front .wordmark { left: 114px; top: 104px; font-size: 52px; color: var(--ink); }
  .tagline { position: absolute; right: 44px; top: 196px; text-align: right; }
  .tagline-company { color: var(--accent); font-size: 17px; letter-spacing: 0.02em; }
  .tagline-services { color: var(--ink); font-weight: 700; font-size: 17px; margin-top: 2px; }

  /* Back */
  .back-art { position: absolute; inset: 0; width: 100%; height: 100%; }
  .card-back .brand-mark { left: 40px; top: 52px; width: 26px; height: 26px; }
  .card-back .wordmark { left: 80px; top: 48px; font-size: 26px; color: var(--white); }
  .licence { position: absolute; right: 36px; top: 24px; font-size: 12px; }
  .licence-label { color: var(--accent-light); font-weight: 700; }
  .person { position: absolute; right: 52px; top: 140px; text-align: right; }
  .person-name { color: var(--accent-light); font-weight: 700; font-size: 21px; letter-spacing: 0.02em; }
  .person-role { font-size: 13px; margin-top: -2px; }
  .contact { position: absolute; left: 52px; top: 210px; list-style: none; }
  .contact li { display: flex; align-items: center; gap: 10px; color: var(--accent-light); font-size: 15px; line-height: 24px; }
  .contact svg { width: 14px; height: 14px; flex: none; }
  .follow {
    position: absolute; right: 30px; top: 262px;
    display: flex; align-items: center; gap: 6px;
    color: var(--ink); font-size: 12px;
  }
  .follow-handle { font-weight: 700; }
  .social-square {
    width: 13px; height: 13px; border-radius: 3px;
    background: var(--ink); flex: none;
  }
</style>
</head>
<body>

  <section class="card card-front" aria-label="Card front">
    <span class="brand-mark" aria-hidden="true"></span>
    <div class="wordmark">VELMOR.</div>
    <div class="tagline">
      <div class="tagline-company">VELMOR CONSTRUCT</div>
      <div class="tagline-services">Carpentry &amp; Building Services</div>
    </div>
  </section>

  <section class="card card-back" aria-label="Card back">
    <svg class="back-art" viewBox="0 0 540 310" preserveAspectRatio="none" aria-hidden="true">
      <defs>
        <linearGradient id="band-gradient" x1="0" y1="1" x2="1" y2="0">
          <stop offset="0" stop-color="#cfcfcf"/>
          <stop offset="0.45" stop-color="#a6a6a6"/>
          <stop offset="1" stop-color="#9a9a9a"/>
        </linearGradient>
      </defs>
      <line x1="40" y1="190" x2="470" y2="190" stroke="#8c8c8c" stroke-width="1"/>
      <path d="M0,286 C200,286 300,256 370,221 C430,196 480,189 540,189 L540,310 L0,310 Z" fill="#ffffff"/>
      <path d="M0,292 C200,292 300,262 370,227 C430,202 480,196 540,196 L540,310 L0,310 Z" fill="#000000"/>
      <path d="M0,300 C200,300 300,270 370,235 C430,210 480,205 540,205 L540,310 L0,310 Z" fill="url(#band-gradient)"/>
    </svg>

    <span class="brand-mark" aria-hidden="true"></span>
    <div class="wordmark">VELMOR.</div>

    <div class="licence"><span class="licence-label">Lic No.</span> 718263D</div>

    <div class="person">
      <div class="person-name">Nilo Petrakis</div>
      <div class="person-role">Owner</div>
    </div>

    <ul class="contact">
      <li>
        <svg viewBox="0 0 16 16" aria-hidden="true"><path d="M4 1.5 L6.5 4.5 L5 6.3 C5.8 8 7.8 10 9.7 11 L11.5 9.5 L14.5 12 L13 14.3 C8 14.5 1.5 8 1.7 3 Z" fill="none" stroke="#ffffff" stroke-width="1.4" stroke-linejoin="round"/></svg>
        0481236574
      </li>
      <li>
        <svg viewBox="0 0 16 16" aria-hidden="true"><rect x="1.5" y="3.5" width="13" height="9" fill="none" stroke="#ffffff" stroke-width="1.3"/><path d="M1.5 3.5 L8 9 L14.5 3.5" fill="none" stroke="#ffffff" stroke-width="1.3"/></svg>
        Velmorconstruct@brixmail.com
      </li>
    </ul>

    <div class="follow">
      <span>Follow us on</span>
      <span class="social-square" role="img" aria-label="Facebook"></span>
      <span class="social-square" role="img" aria-label="Instagram"></span>
      <span class="follow-handle">@velmorconstruct</span>
    </div>
  </section>

</body>
</html>
```